Website Required for Small Cyber Security Company

Require a website for Cyber Security company. I have logo which i will attach. Please use logo blue and white as a guide
Would ultimately like the site to have a technology theme with the following pages Landing page
Services
Contact
Careers

I can provide content for each of those pages in due course, until then happy for you to use dummy data to display purposes

Target Market(s)

Government

Industry/Entity Type

Cyber Security

Coding

Coded - Design and coding required

Number of Pages Required

4 page

Colors
0054AA
0677BA
7BADD7
CADEEF
E8F1F8

Requirements
Must have
• High quality finish and UX
Nice to have
• look and feel professional and not cheap

```html
<!DOCTYPE html>
<html lang="en">
<head>
<meta charset="utf-8">
<title>Harrow Point Consulting – Cybersecurity Services</title>
<link href="https://fonts.googleapis.com/css2?family=Roboto:wght@300;400;500;700;900&display=swap" rel="stylesheet">
<style>
:root{
  --navy:#0a1c55;
  --navy-deep:#061241;
  --blue:#0054AA;
  --blue-mid:#0677BA;
  --blue-soft:#7BADD7;
  --blue-pale:#CADEEF;
  --blue-wash:#E8F1F8;
  --ink:#1b2340;
  --text:#5a6378;
  --white:#ffffff;
}
*{box-sizing:border-box;margin:0;padding:0}
html,body{width:1200px;height:4048px;overflow:hidden}
body{font-family:"Roboto",Arial,sans-serif;color:var(--text);background:var(--white);font-size:14px;line-height:1.55;position:relative}
section,header,footer{position:relative;width:1200px;overflow:hidden}
h1,h2,h3,h4{color:var(--ink);font-weight:700;line-height:1.2}
.btn{display:inline-block;border:2px solid var(--white);color:var(--white);font-weight:700;font-size:12px;letter-spacing:1px;padding:11px 26px;border-radius:24px;text-decoration:none}
.btn--blue{border-color:var(--blue);color:var(--blue)}
.btn--solid{background:var(--blue);border-color:var(--blue);color:var(--white)}
.media{position:absolute}

/* Hero */
.hero{height:600px;background:radial-gradient(circle at 75% 35%,#1d5fc4 0%,#0d3590 35%,var(--navy) 70%,var(--navy-deep) 100%)}
.brand{position:absolute;left:150px;top:22px;display:flex;align-items:center;gap:12px;color:var(--white)}
.brand__mark{width:44px;height:44px;border-radius:50%;background:var(--blue-mid)}
.brand__name{font-size:26px;font-weight:900;letter-spacing:1px;line-height:1}
.brand__sub{font-size:11px;letter-spacing:5px;font-weight:400;color:var(--blue-pale);display:block;margin-top:4px}
.nav{position:absolute;right:150px;top:26px;display:flex;gap:26px}
.nav a{color:var(--white);font-size:13px;font-weight:700;text-decoration:none;letter-spacing:.5px}
.hero__copy{position:absolute;left:160px;top:270px}
.hero__title{color:var(--white);font-size:32px;font-weight:900;line-height:1.15}
.hero__title span{display:block;font-weight:400;font-size:30px}
.hero__copy .btn{margin-top:32px}
.hero__art{left:560px;top:40px;width:600px;height:520px;border-radius:24px;background:radial-gradient(circle at 50% 50%,#3c8fe6 0%,#1856b8 45%,rgba(13,53,144,0) 75%)}

/* Features */
.features{height:240px;background:var(--white)}
.features__row{position:absolute;left:150px;top:20px;display:flex;gap:12px}
.feature{width:216px;height:190px;background:var(--blue-wash);border:1px solid var(--blue-pale);border-radius:6px;padding:22px 18px;text-align:center}
.feature svg{width:44px;height:44px}
.feature h3{font-size:15px;margin:12px 0 8px}
.feature p{font-size:12px;line-height:1.5}

/* Welcome */
.welcome{height:480px}
.welcome__art{left:160px;top:20px;width:440px;height:420px;clip-path:polygon(50% 0,100% 25%,100% 75%,50% 100%,0 75%,0 25%);background:linear-gradient(150deg,#0d2a6e,#2a6fc9 55%,#7BADD7)}
.welcome__text{position:absolute;left:640px;top:30px;width:420px}
.eyebrow{color:var(--blue);font-size:16px;font-weight:700;letter-spacing:1px}
.welcome__text h2{font-size:30px;font-weight:900;margin:4px 0 14px}
.welcome__text p{font-size:13px}
.ticks{list-style:none;margin:18px 0 24px}
.ticks li{display:flex;align-items:center;gap:10px;font-size:13px;color:var(--ink);margin-bottom:10px}
.ticks svg{width:18px;height:18px;flex:none}

/* Protection */
.protection{height:580px}
.protection__text{position:absolute;left:160px;top:30px;width:460px}
.protection__text h2{font-size:26px;margin-bottom:14px}
.protection__text>p{font-size:13px}
.grid{display:grid;grid-template-columns:1fr 1fr;gap:14px;margin-top:24px}
.tile{background:var(--blue-wash);border-radius:6px;padding:18px;height:150px}
.tile svg{width:30px;height:30px}
.tile h3{font-size:14px;margin:8px 0 6px}
.tile p{font-size:12px;line-height:1.5}
.protection__art{left:652px;top:30px;width:548px;height:500px;background:linear-gradient(160deg,#0a1330,#1c2f6a 50%,#2e5aa8)}

/* Testimonials */
.testimonials{height:440px;background:linear-gradient(90deg,#1a5fb8,#3a86d4 50%,#1a5fb8);text-align:center;color:var(--white)}
.testimonials .eyebrow{color:var(--blue-pale);font-size:15px;font-weight:400;padding-top:60px}
.testimonials h2{color:var(--white);font-size:40px;font-weight:900;letter-spacing:1px}
.testimonials blockquote{width:720px;margin:26px auto 0;font-size:13px;line-height:1.7;color:#e6f0fb}
.quote{position:absolute;top:150px;font-size:90px;font-weight:900;color:rgba(255,255,255,.55);line-height:1}
.quote--l{left:180px}.quote--r{right:180px}
.arrow{position:absolute;top:205px;width:36px;height:36px}
.arrow--l{left:40px}.arrow--r{right:40px}
.client{margin-top:22px;display:flex;flex-direction:column;align-items:center}
.client__avatar{width:56px;height:56px;border-radius:50%;background:var(--blue-pale);border:3px solid var(--white)}
.client__name{font-weight:700;margin-top:8px;font-size:14px}
.client__role{font-size:11px;color:var(--blue-pale)}

/* Why */
.why{height:560px}
.why__art{left:0;top:40px;width:560px;height:480px;background:linear-gradient(135deg,#0b1f5c,#3067c4 55%,#9cc3ea)}
.why__text{position:absolute;left:608px;top:50px;width:440px}
.why__text h2{font-size:38px;margin-bottom:12px}
.why__text>p{font-size:13px}
.point{display:flex;gap:16px;padding:18px 0;border-bottom:1px solid var(--blue-pale)}
.point__icon{width:54px;height:54px;flex:none;border-radius:6px;background:var(--blue-wash);display:flex;align-items:center;justify-content:center}
.point__icon svg{width:28px;height:28px}
.point h3{font-size:15px;margin-bottom:4px}
.point p{font-size:12px;line-height:1.5}

/* Blog */
.blog{height:540px}
.blog h2{text-align:center;font-size:40px;font-weight:900;padding-top:20px}
.blog__row{position:absolute;left:150px;top:100px;display:flex;gap:20px}
.post{width:286px;height:410px;background:var(--white);border-radius:10px;box-shadow:0 6px 24px rgba(0,40,100,.15);overflow:hidden;text-align:center}
.post__img{height:180px}
.post__img--a{background:linear-gradient(150deg,#0b2a74,#2b7ad6)}
.post__img--b{background:linear-gradient(150deg,#1d2e52,#5f86b9)}
.post__img--c{background:linear-gradient(150deg,#0a1440,#2e4fa0)}
.post h3{font-size:14px;padding:18px 24px 4px}
.post time{font-size:11px;color:var(--blue-mid)}
.post p{font-size:12px;padding:6px 24px 14px;line-height:1.5}
.blog .arrow{top:290px}
.blog .arrow--l{left:110px}.blog .arrow--r{right:110px}

/* Footer */
.footer{height:608px;background:linear-gradient(180deg,#0a2270,var(--navy-deep));color:#c9d6f2}
.follow{text-align:center;padding-top:40px}
.follow .eyebrow{color:var(--blue-soft);font-size:13px;font-weight:400}
.follow h2{color:var(--white);font-size:40px;font-weight:900}
.follow p{width:720px;margin:12px auto 0;font-size:13px}
.socials{display:flex;justify-content:center;gap:12px;margin-top:22px}
.socials span{width:34px;height:34px;border-radius:50%;border:2px solid var(--white)}
.cols{position:absolute;left:150px;top:330px;display:flex;gap:60px}
.col{width:260px}
.col__kicker{font-size:11px;color:var(--blue-soft);letter-spacing:1px}
.col h3{color:var(--white);font-size:22px;font-weight:900;margin-bottom:16px}
.col p,.col li{font-size:12px;margin-bottom:10px}
.contact-line{display:flex;gap:10px;align-items:flex-start}
.contact-line svg{width:16px;height:16px;flex:none;margin-top:2px}
.col ul{list-style:none}
.col li::before{content:"›";color:var(--blue-soft);margin-right:8px}
.field{width:100%;height:40px;border-radius:4px;background:var(--white);color:#8893a8;font-size:12px;padding:11px 14px;margin:8px 0 12px}
.footer .btn--solid{width:100%;text-align:center;border-radius:4px}
.copyright{position:absolute;left:0;bottom:0;width:1200px;height:56px;background:#0f3aa0;color:#dbe6fa;font-size:12px;text-align:center;line-height:56px}
</style>
</head>
<body>

<header class="hero">
  <div class="brand">
    <span class="brand__mark"></span>
    <div><span class="brand__name">HARROW POINT</span><span class="brand__sub">CONSULTING</span></div>
  </div>
  <nav class="nav"><a href="#">HOME</a><a href="#">SERVICES</a><a href="#">CAREERS</a><a href="#">CONTACT US</a></nav>
  <div class="hero__copy">
    <h1 class="hero__title">WE PROVIDE MOST ADVANCED<span>CYBERSECURITY SERVICES</span></h1>
    <a class="btn" href="#">GET A QUOTE</a>
  </div>
  <div class="media hero__art" role="img" aria-label="Isometric illustration of a laptop protected by a glowing security shield, padlock and gears"></div>
</header>

<section class="features">
  <div class="features__row">
    <article class="feature">
      <svg viewBox="0 0 24 24" fill="none" stroke="#0054AA" stroke-width="1.6"><path d="M12 2l8 3v6c0 5-3.5 9-8 11-4.5-2-8-6-8-11V5z"/><path d="M8.5 12l2.5 2.5 4.5-5"/></svg>
      <h3>Security Solutions</h3>
      <p>Lorem ipsum is simply dummy text of the printing and typesetting industry.</p>
    </article>
    <article class="feature">
      <svg viewBox="0 0 24 24" fill="none" stroke="#0054AA" stroke-width="1.6"><circle cx="11" cy="11" r="7"/><path d="M16 16l5 5"/></svg>
      <h3>Cyber Threat Hunting</h3>
      <p>Lorem ipsum is simply dummy text of the printing and typesetting industry.</p>
    </article>
    <article class="feature">
      <svg viewBox="0 0 24 24" fill="none" stroke="#0054AA" stroke-width="1.6"><rect x="3" y="4" width="18" height="12" rx="1"/><path d="M8 20h8M12 16v4"/></svg>
      <h3>Pen Testing</h3>
      <p>Lorem ipsum is simply dummy text of the printing and typesetting industry.</p>
    </article>
    <article class="feature">
      <svg viewBox="0 0 24 24" fill="none" stroke="#0054AA" stroke-width="1.6"><circle cx="12" cy="9" r="6"/><path d="M8 14l-2 8 6-3 6 3-2-8"/></svg>
      <h3>Industry Certified</h3>
      <p>Lorem ipsum is simply dummy text of the printing and typesetting industry.</p>
    </article>
  </div>
</section>

<section class="welcome">
  <div class="media welcome__art" role="img" aria-label="Hexagon photo of hands on a keyboard with digital security icons"></div>
  <div class="welcome__text">
    <p class="eyebrow">WELCOME TO</p>
    <h2>HARROW POINT CONSULTING</h2>
    <p>Lorem Ipsum is simply dummy text of the printing and typesetting industry. Lorem Ipsum has been the industry's standard dummy text ever since the 1500s, when an unknown printer took a galley of type and scrambled it to make a type specimen book. It has survived not only five centuries, but also the leap into electronic typesetting.</p>
    <ul class="ticks">
      <li><svg viewBox="0 0 20 20"><circle cx="10" cy="10" r="10" fill="#0054AA"/><path d="M6 10l3 3 5-6" stroke="#fff" stroke-width="2" fill="none"/></svg>Providing Experience &amp; Consolidations</li>
      <li><svg viewBox="0 0 20 20"><circle cx="10" cy="10" r="10" fill="#0054AA"/><path d="M6 10l3 3 5-6" stroke="#fff" stroke-width="2" fill="none"/></svg>Best Networking &amp; Security Solutions</li>
      <li><svg viewBox="0 0 20 20"><circle cx="10" cy="10" r="10" fill="#0054AA"/><path d="M6 10l3 3 5-6" stroke="#fff" stroke-width="2" fill="none"/></svg>Affordable Security Packages &amp; Detailed Results</li>
      <li><svg viewBox="0 0 20 20"><circle cx="10" cy="10" r="10" fill="#0054AA"/><path d="M6 10l3 3 5-6" stroke="#fff" stroke-width="2" fill="none"/></svg>It is a long established fact that a reader will</li>
    </ul>
    <a class="btn btn--blue" href="#">READ MORE</a>
  </div>
</section>

<section class="protection">
  <div class="protection__text">
    <h2>The Most Complete And Effective Protection For Your Home And Office</h2>
    <p>Lorem Ipsum is simply dummy text of the printing and typesetting industry. Lorem Ipsum has been the industry's standard dummy text ever since the 1500s, when an unknown printer took a galley of type.</p>
    <div class="grid">
      <div class="tile">
        <svg viewBox="0 0 24 24" fill="none" stroke="#0054AA" stroke-width="1.6"><circle cx="11" cy="11" r="7"/><path d="M16 16l5 5"/></svg>
        <h3>Check And Search Hazards</h3>
        <p>Lorem ipsum is simply dummy text of the printing and typesetting industry.</p>
      </div>
      <div class="tile">
        <svg viewBox="0 0 24 24" fill="none" stroke="#0054AA" stroke-width="1.6"><rect x="3" y="4" width="18" height="12" rx="1"/><path d="M8 20h8M12 16v4"/></svg>
        <h3>Install And Configure Software</h3>
        <p>Lorem ipsum is simply dummy text of the printing and typesetting industry.</p>
      </div>
      <div class="tile">
        <svg viewBox="0 0 24 24" fill="none" stroke="#0054AA" stroke-width="1.6"><circle cx="12" cy="8" r="4"/><path d="M4 21c0-4.5 3.5-7 8-7s8 2.5 8 7"/></svg>
        <h3>Departure Of Our Experts</h3>
        <p>Lorem ipsum is simply dummy text of the printing and typesetting industry.</p>
      </div>
      <div class="tile">
        <svg viewBox="0 0 24 24" fill="none" stroke="#0054AA" stroke-width="1.6"><path d="M4 14v-2a8 8 0 0116 0v2"/><rect x="3" y="13" width="4" height="6" rx="1"/><rect x="17" y="13" width="4" height="6" rx="1"/></svg>
        <h3>24/7 Support &amp; Remote Admin</h3>
        <p>Lorem ipsum is simply dummy text of the printing and typesetting industry.</p>
      </div>
    </div>
  </div>
  <div class="media protection__art" role="img" aria-label="Photo of a hooded figure working at a laptop in a dark room with code in the background"></div>
</section>

<section class="testimonials">
  <p class="eyebrow">OUR CLIENT SAYING</p>
  <h2>TESTIMONIALS</h2>
  <span class="quote quote--l">“</span><span class="quote quote--r">”</span>
  <svg class="arrow arrow--l" viewBox="0 0 24 24" fill="none" stroke="#fff" stroke-width="2"><path d="M15 5l-7 7 7 7"/></svg>
  <svg class="arrow arrow--r" viewBox="0 0 24 24" fill="none" stroke="#fff" stroke-width="2"><path d="M9 5l7 7-7 7"/></svg>
  <blockquote>Lorem ipsum dolor sit amet, consectetur adipiscing elit. Sed blandit posuere erat, non pretium felis tempor sed. Integer vestibulum rhoncus lorem, vitae fermentum lectus faucibus nec. Nullam sed nibh in lacus aliquet gravida a at diam. Pellentesque habitant morbi tristique senectus et netus et malesuada fames ac turpis egestas. Donec vel est eget metus vulputate convallis non eu magna.</blockquote>
  <div class="client">
    <span class="client__avatar"></span>
    <span class="client__name">MARISA T.</span>
    <span class="client__role">Happy Customer</span>
  </div>
</section>

<section class="why">
  <div class="media why__art" role="img" aria-label="Photo of a hand touching a glowing digital fingerprint over a keyboard"></div>
  <div class="why__text">
    <h2>Why choose us</h2>
    <p>Lorem Ipsum is simply dummy text of the printing and typesetting industry. Lorem Ipsum has been the industry's standard dummy text ever since the 1500s, when an unknown printer took a galley of type and scrambled it to make a type specimen book.</p>
    <div class="point">
      <div class="point__icon"><svg viewBox="0 0 24 24" fill="none" stroke="#0054AA" stroke-width="1.6"><path d="M3 11l9-7 9 7v9H3z"/><path d="M10 20v-5h4v5"/></svg></div>
      <div><h3>Keep safe your family exploring the internet</h3><p>Lorem ipsum is simply dummy text of the printing and typesetting industry.</p></div>
    </div>
    <div class="point">
      <div class="point__icon"><svg viewBox="0 0 24 24" fill="none" stroke="#0054AA" stroke-width="1.6"><path d="M4 14v-2a8 8 0 0116 0v2"/><rect x="3" y="13" width="4" height="6" rx="1"/><rect x="17" y="13" width="4" height="6" rx="1"/></svg></div>
      <div><h3>24/7 Cyber Security Operation Center</h3><p>Lorem ipsum is simply dummy text of the printing and typesetting industry.</p></div>
    </div>
    <div class="point">
      <div class="point__icon"><svg viewBox="0 0 24 24" fill="none" stroke="#0054AA" stroke-width="1.6"><rect x="5" y="10" width="14" height="11" rx="1"/><path d="M8 10V7a4 4 0 018 0v3"/></svg></div>
      <div><h3>The Perfect Solution For all Protection</h3><p>Lorem ipsum is simply dummy text of the printing and typesetting industry.</p></div>
    </div>
  </div>
</section>

<section class="blog">
  <h2>LATEST BLOG</h2>
  <svg class="arrow arrow--l" viewBox="0 0 24 24" fill="none" stroke="#1b2340" stroke-width="2"><path d="M15 5l-7 7 7 7"/></svg>
  <svg class="arrow arrow--r" viewBox="0 0 24 24" fill="none" stroke="#1b2340" stroke-width="2"><path d="M9 5l7 7-7 7"/></svg>
  <div class="blog__row">
    <article class="post">
      <div class="post__img post__img--a" role="img" aria-label="Illustration of a security shield with a tick on a circuit background"></div>
      <h3>LOREM IPSUM DOLOR SIT AMETCONSECTETUR</h3>
      <time>Date : 05.06.2023</time>
      <p>Lorem ipsum dolor sit amet, consectetur adipiscing elit. Etiam id nulla tincidunt, efficitur risus sit amet.</p>
      <a class="btn btn--solid" href="#">LEARN MORE</a>
    </article>
    <article class="post">
      <div class="post__img post__img--b" role="img" aria-label="Photo of a person working on a laptop in an office"></div>
      <h3>LOREM IPSUM DOLOR SIT AMETCONSECTETUR</h3>
      <time>Date : 05.06.2023</time>
      <p>Lorem ipsum dolor sit amet, consectetur adipiscing elit. Etiam id nulla tincidunt, efficitur risus sit amet.</p>
      <a class="btn btn--solid" href="#">LEARN MORE</a>
    </article>
    <article class="post">
      <div class="post__img post__img--c" role="img" aria-label="Photo of a hooded figure in front of a blue digital screen"></div>
      <h3>LOREM IPSUM DOLOR SIT AMETCONSECTETUR</h3>
      <time>Date : 05.06.2023</time>
      <p>Lorem ipsum dolor sit amet, consectetur adipiscing elit. Etiam id nulla tincidunt, efficitur risus sit amet.</p>
      <a class="btn btn--solid" href="#">LEARN MORE</a>
    </article>
  </div>
</section>

<footer class="footer">
  <div class="follow">
    <p class="eyebrow">SOCIAL PROFILES</p>
    <h2>FOLLOW US</h2>
    <p>Lorem Ipsum is simply dummy text of the printing and typesetting industry. Lorem Ipsum has been the industry's standard dummy text ever since the 1500s, when an unknown printer took a galley of type and scrambled it to make a type specimen book.</p>
    <div class="socials"><span></span><span></span><span></span><span></span><span></span></div>
  </div>
  <div class="cols">
    <div class="col">
      <p class="col__kicker">FEEL FREE TO</p>
      <h3>CONTACT US</h3>
      <p class="contact-line"><svg viewBox="0 0 24 24" fill="none" stroke="#7BADD7" stroke-width="2"><path d="M12 22s7-7 7-12a7 7 0 00-14 0c0 5 7 12 7 12z"/><circle cx="12" cy="10" r="2.5"/></svg>Lorem ipsum is simply dummy text of the printing and typesetting industry.</p>
      <p class="contact-line"><svg viewBox="0 0 24 24" fill="none" stroke="#7BADD7" stroke-width="2"><rect x="3" y="5" width="18" height="14" rx="1"/><path d="M3 6l9 7 9-7"/></svg>hello@harrowpoint.example</p>
      <p class="contact-line"><svg viewBox="0 0 24 24" fill="none" stroke="#7BADD7" stroke-width="2"><circle cx="12" cy="12" r="9"/><path d="M3 12h18M12 3c3 3 3 15 0 18M12 3c-3 3-3 15 0 18"/></svg>www.harrowpoint.example</p>
    </div>
    <div class="col">
      <p class="col__kicker">OUR</p>
      <h3>QUICK LINKS</h3>
      <ul><li>Home</li><li>About</li><li>Services</li><li>Careers</li><li>Contact Us</li><li>Privacy Policy</li><li>Terms and conditions</li></ul>
    </div>
    <div class="col">
      <p class="col__kicker">SIGNUP FOR</p>
      <h3>NEWSLETTER</h3>
      <p>Lorem Ipsum is simply dummy text of the printing and typesetting industry. Lorem Ipsum industry standard text.</p>
      <div class="field">Enter your email id</div>
      <a class="btn btn--solid" href="#">SUBSCRIBE NOW</a>
    </div>
  </div>
  <p class="copyright">© Copyright 2023 harrowpoint.example | All Rights Reserved</p>
</footer>

</body>
</html>
```